8x8 Social Media Ad - Harbor Summit Expo

Attention Real Estate Agents
Please join us for our
Quarterly Real Estate Training Expo
The 2nd Saturday of February, May, August and November
Our Next Training Expo is _________________________________
From 9 am to 1 pm
at
Marlowe Suites Fernridge Station
4187 Copperleaf Lane, Greenbelt, MD 20770
Scheduled Speakers
9:00 am - Desmond Pryce - Orientation
9:30 am - Terrell Oakes - Multiple Income Streams / Keystone Track
10:00 am - Lorna Beckett - Marketing though Social Media
10:45 am - Raul Denning - Generating Business through Kelp-Nest
11:30 am - Tunde Adesemi - Real Estate Investing
12:15 pm - Marcus Oyelowo - (Main Speaker) Training Topic TBA
For more information call Desmond Pryce at (240) 555-0192 or email dpryce@harborsummithomes.example

```html
<!DOCTYPE html>
<html lang="en">
<head>
<meta charset="utf-8">
<title>Harbor Summit Expo – Quarterly Real Estate Training Expo</title>
<link href="https://fonts.googleapis.com/css2?family=Roboto:wght@700;900&family=Montserrat:wght@500;600;700;800&family=Kaushan+Script&display=swap" rel="stylesheet">
<style>
  :root{
    --teal:#267a78;
    --teal-deep:#1f6b69;
    --teal-bright:#1a9492;
    --teal-text:#1c7f7d;
    --ink:#1d2b2b;
    --white:#ffffff;
    --pill:#eef1f1;
    --photo-a:#e4e7e7;
    --photo-b:#8c9596;
  }
  *{box-sizing:border-box;margin:0;padding:0}
  html,body{width:1200px;height:1200px;overflow:hidden;background:#fff}
  .ad{position:relative;width:1200px;height:1200px;overflow:hidden;background:var(--white);font-family:"Montserrat",sans-serif;color:var(--ink)}
  .hero-bg{position:absolute;left:0;top:0;width:1200px;height:690px;
    background:linear-gradient(180deg,#2a7d7b 0%,#267573 55%,#2b7f7c 100%)}
  .hero-bg::after{content:"";position:absolute;left:0;right:0;bottom:0;height:70px;
    background:linear-gradient(180deg,rgba(255,255,255,0) 0%,#fff 100%)}
  .lower-bg{position:absolute;left:0;top:690px;width:1200px;height:510px;
    background:linear-gradient(180deg,#fff 0%,#f3f5f6 60%,#eef1f2 100%)}
  .intro{position:absolute;top:42px;width:100%;text-align:center;color:var(--white);font-weight:600;font-size:21px}
  .headline{position:absolute;top:70px;width:100%;text-align:center;color:var(--white);
    font-family:"Roboto",sans-serif;font-weight:900;font-size:76px;letter-spacing:0.5px;line-height:1}
  .headline-script{position:absolute;top:150px;width:100%;text-align:center;color:var(--white);
    font-family:"Kaushan Script",cursive;font-size:90px;line-height:1.1}
  .date-pill{position:absolute;left:190px;top:285px;width:820px;height:47px;background:var(--pill);
    border-radius:6px 24px 24px 6px;display:flex;align-items:center;padding-left:20px;
    font-size:23px;color:var(--teal-text);font-weight:500}
  .date-pill strong{font-weight:800;margin-left:12px}
  .time{position:absolute;top:350px;width:100%;text-align:center;color:var(--white);font-weight:800;font-size:44px;
    text-shadow:2px 3px 4px rgba(0,0,0,.45)}
  .speaker-card{position:absolute;top:432px;width:204px;height:306px;border-radius:86px 86px 0 0;
    border:7px solid var(--teal-bright);border-left-width:0;border-bottom-width:2px;overflow:hidden}
  .speaker-card .photo{width:100%;height:100%;border-radius:80px 80px 0 0;
    background:linear-gradient(160deg,var(--photo-a) 0%,#c3c9ca 45%,var(--photo-b) 100%)}
  .schedule-label{position:absolute;left:110px;top:828px;width:164px;text-align:center;font-size:20px;font-weight:500;line-height:29px}
  .schedule-label svg{display:block;margin:0 auto 6px}
  .divider{position:absolute;width:1px;background:#b8c2c2}
  .col{position:absolute;top:774px;list-style:none;font-size:19px;font-weight:500}
  .col li{height:35px;line-height:24px;white-space:nowrap}
  .col.times{left:334px;color:var(--teal-text)}
  .col.names{left:470px}
  .col.topics{left:670px}
  .venue-band{position:absolute;left:0;top:1002px;width:1200px;height:43px;
    background:linear-gradient(90deg,var(--teal-deep),var(--teal-bright));
    display:flex;align-items:center;justify-content:center;gap:12px;color:var(--white);font-size:19.5px;font-weight:600}
  .brand{position:absolute;left:34px;top:1066px;width:210px;height:106px;display:flex;align-items:center;justify-content:center;
    text-align:center;font-weight:800;font-size:20px;line-height:1.25;color:var(--teal-text)}
  .info-line{position:absolute;left:332px;top:1078px;font-size:20px;font-weight:500;white-space:nowrap}
  .contact-pill{position:absolute;left:625px;top:1071px;width:469px;height:39px;background:var(--teal-bright);
    border-radius:10px 20px 20px 10px;color:var(--white);font-size:21px;font-weight:700;
    display:flex;align-items:center;justify-content:center;gap:6px}
  .contact-pill .mid{font-weight:500}
  .web-row{position:absolute;top:1131px;font-size:16.5px;font-weight:500;display:flex;align-items:center;gap:9px;white-space:nowrap}
  .web-row.email{left:333px}
  .web-row.site{left:800px}
</style>
</head>
<body>
<main class="ad">
  <div class="hero-bg" role="img" aria-label="Faded photo of a two-storey house with trees, tinted teal"></div>
  <div class="lower-bg"></div>

  <p class="intro">Please join us for our</p>
  <h1 class="headline">QUARTERLY REAL ESTATE</h1>
  <p class="headline-script">Training Expo</p>
  <div class="date-pill">The 2nd Saturday of <strong>February, May, August and November</strong></div>
  <p class="time">From 9 am to 1 pm</p>

  <div class="speaker-card" style="left:56px"><div class="photo" role="img" aria-label="Portrait photo of two speakers"></div></div>
  <div class="speaker-card" style="left:279px"><div class="photo" role="img" aria-label="Portrait photo of a speaker in a hat and dark jacket"></div></div>
  <div class="speaker-card" style="left:502px"><div class="photo" role="img" aria-label="Portrait photo of a speaker in a denim shirt"></div></div>
  <div class="speaker-card" style="left:725px"><div class="photo" role="img" aria-label="Portrait photo of a speaker in a blue suit"></div></div>
  <div class="speaker-card" style="left:948px"><div class="photo" role="img" aria-label="Portrait photo of a speaker in a dark blazer"></div></div>

  <div class="schedule-label">
    <svg width="22" height="24" viewBox="0 0 22 24" aria-hidden="true"><circle cx="11" cy="6" r="6" fill="#1a9492"/><path d="M0 24v-4c0-4 4-6 11-6s11 2 11 6v4z" fill="#1a9492"/></svg>
    Scheduled<br>Speakers
  </div>
  <div class="divider" style="left:303px;top:778px;height:190px"></div>
  <div class="divider" style="left:446px;top:778px;height:190px"></div>
  <div class="divider" style="left:648px;top:778px;height:190px"></div>

  <ul class="col times"><li>9:00 am</li><li>9:30 am</li><li>10:00 am</li><li>10:45 am</li><li>11:30 am</li><li>12:15 pm</li></ul>
  <ul class="col names"><li>Desmond Pryce</li><li>Terrell Oakes</li><li>Lorna Beckett</li><li>Raul Denning</li><li>Tunde Adesemi</li><li>Marcus Oyelowo</li></ul>
  <ul class="col topics"><li>Orientation</li><li>Multiple Income Streams / Keystone Track</li><li>Marketing though Social Media</li><li>Generating Business through Kelp-Nest</li><li>Real Estate Investing</li><li>(Main Speaker) Training Topic TBA</li></ul>

  <div class="venue-band">
    <svg width="18" height="24" viewBox="0 0 18 24" aria-hidden="true"><path d="M9 0a9 9 0 0 0-9 9c0 7 9 15 9 15s9-8 9-15a9 9 0 0 0-9-9z" fill="#fff"/><circle cx="9" cy="9" r="3.5" fill="#1f6b69"/></svg>
    Marlowe Suites Fernridge Station 4187 Copperleaf Lane, Greenbelt, MD 20770
  </div>

  <div class="brand">Harbor Summit<br>Realty Group</div>
  <div class="divider" style="left:303px;top:1091px;height:68px"></div>

  <p class="info-line">For more information call</p>
  <div class="contact-pill">Desmond Pryce <span class="mid">at</span> (240) 555-0192</div>

  <div class="web-row email">
    <svg width="16" height="11" viewBox="0 0 17 12" aria-hidden="true"><rect width="17" height="12" fill="#1a9492"/><path d="M0 0l8.5 7L17 0" stroke="#fff" stroke-width="1.4" fill="none"/></svg>
    email dpryce@harborsummithomes.example
  </div>
  <div class="web-row site">
    <svg width="14" height="14" viewBox="0 0 14 14" aria-hidden="true"><circle cx="7" cy="7" r="6.3" fill="none" stroke="#1a9492" stroke-width="1.4"/><path d="M0.7 7h12.6M7 .7c-3 3.5-3 9 0 12.6M7 .7c3 3.5 3 9 0 12.6" stroke="#1a9492" stroke-width="1.1" fill="none"/></svg>
    www.harborsummithomes.example
  </div>
</main>
</body>
</html>
```